2in1 Bartender & Sommelier needs a business card

I need a business card. I worked as a bartender in many places but I just finished a sommelier school and I would like a new business card. I like minimal design, natural materials and something what makes the people think :) I try to be creative in cocktail making, like little mixology, little twist on recipes... I like to travel and discover new places, cultures and of course interesting drinks and improve continously...live a little bit crazy life. And I like what I do...

Target Market(s)

restaurant/winebar managers, winemakers, other sommeliers and bartenders, people who work in food and beverage sector

Industry/Entity Type

Hospitality

Contact Information for Business Card

Rozsa Tarkany
Bartender & Sommelier
Phone: (FR) +33 6 4827 3190
(HU) +36 70 918 6352

Font styles to use
Script

Requirements
Must have
• Some sign, I am a bartender and sommelier as well.
Nice to have
• black and white maybe with 1 or 2 extra color
Should not have
• very colourful, to many things on the card

```html
<!DOCTYPE html>
<html lang="en">
<head>
<meta charset="utf-8">
<title>Rozsa Tarkany – Bartender &amp; Sommelier</title>
<link href="https://fonts.googleapis.com/css2?family=Dancing+Script:wght@500&family=Open+Sans:wght@300;400&display=swap" rel="stylesheet">
<style>
  :root {
    --backdrop: #e9e9e7;
    --card-light: #fbfbfb;
    --card-mid: #e6e7e8;
    --card-edge: #c9cbcd;
    --ink: #1b1b1b;
    --ink-soft: #4a4a4a;
    --accent: #2fc1c6;
  }
  html, body {
    margin: 0;
    padding: 0;
    width: 1200px;
    height: 799px;
    overflow: hidden;
    background: var(--backdrop);
  }
  .business-card {
    position: absolute;
    left: 90px;
    top: 100px;
    width: 1020px;
    height: 599px;
    background: radial-gradient(ellipse at 50% 40%, var(--card-light) 0%, var(--card-mid) 65%, var(--card-edge) 100%);
    box-shadow: 0 6px 22px rgba(0,0,0,0.18);
    text-align: center;
    font-family: "Open Sans", sans-serif;
    color: var(--ink);
  }
  .brand-dot {
    position: absolute;
    left: 50%;
    top: 112px;
    width: 26px;
    height: 26px;
    margin-left: -13px;
    border-radius: 50%;
    background: var(--accent);
  }
  .holder-name {
    position: absolute;
    left: 0;
    right: 0;
    top: 160px;
    margin: 0;
    font-family: "Dancing Script", cursive;
    font-weight: 500;
    font-size: 112px;
    line-height: 1.2;
    color: var(--ink);
  }
  .holder-role {
    position: absolute;
    left: 0;
    right: 0;
    top: 330px;
    margin: 0;
    font-weight: 300;
    font-size: 20px;
    letter-spacing: 4px;
    color: var(--ink-soft);
  }
  .contact {
    position: absolute;
    left: 0;
    right: 0;
    top: 405px;
    margin: 0;
    font-weight: 300;
    font-size: 22px;
    letter-spacing: 3px;
    line-height: 38px;
    color: var(--ink-soft);
  }
</style>
</head>
<body>
  <section class="business-card">
    <span class="brand-dot" aria-hidden="true"></span>
    <h1 class="holder-name">Rozsa Tarkany</h1>
    <p class="holder-role">Bartender &amp; Sommelier</p>
    <p class="contact">
      <span class="contact-label">Phone:</span><br>
      <span class="contact-numbers">(FR) +33 6 4827 3190 | (HU) +36 70 918 6352</span>
    </p>
  </section>
</body>
</html>
```